Book Cover for self help book describing how to become the author of your life

I need a good resolution front cover for a book that is published through Brindlewick in Print and ebook format. I can design the spine and back cover myself so just need the front angle.
The book is titled "Chart New Mornings" and it's about writing your own story for how you want to live your life. The image I had in my mind was a pen writing out the title on the front in a script-like font, like actual handwriting.
I've included a very basic mock-up that I've done myself just to give the general idea. The cover requires three pieces of writing.
Title: Chart New Mornings
Subtitle: Step Into a Brighter Season
Author: Martin Olsfield
Female 35-55

```html
<!DOCTYPE html>
<html lang="en">
<head>
<meta charset="utf-8">
<title>Chart New Mornings – Front Cover</title>
<link rel="stylesheet" href="https://fonts.googleapis.com/css2?family=Caveat+Brush&family=Open+Sans:wght@600;700&display=swap">
<style>
  :root {
    --page-bg: #ffffff;
    --sky-top: #e8c6be;
    --sky-mid: #efdcd2;
    --sky-low: #ece5d6;
    --ink: #1d1d1d;
    --ink-accent: #2f5068;
    --treeline: #50656e;
    --water-top: #7e9aa6;
    --water-bottom: #3c5562;
    --band: #161616;
    --band-text: #ffffff;
    --skin-light: #e9c2a9;
    --skin-dark: #c98f71;
    --figure: #2a2a2c;
  }
  * { margin: 0; padding: 0; box-sizing: border-box; }
  html, body {
    width: 1200px;
    height: 803px;
    overflow: hidden;
    background: var(--page-bg);
  }
  .cover {
    position: absolute;
    left: 340px;
    top: 31px;
    width: 520px;
    height: 740px;
    overflow: hidden;
    box-shadow: 0 6px 22px rgba(0,0,0,0.18);
  }
  .cover__sky {
    position: absolute;
    inset: 0;
    background: linear-gradient(180deg, var(--sky-top) 0%, var(--sky-mid) 35%, var(--sky-low) 68%);
  }
  .cover__hand {
    position: absolute;
    left: 140px;
    top: 0;
    width: 230px;
    height: 200px;
    background: linear-gradient(160deg, var(--skin-light) 0%, var(--skin-dark) 100%);
    border-radius: 0 0 50px 80px;
    opacity: 0.85;
  }
  .cover__landscape {
    position: absolute;
    left: 0;
    bottom: 0;
    width: 100%;
    height: 250px;
    background: linear-gradient(180deg, var(--treeline) 0%, var(--water-top) 18%, var(--water-bottom) 100%);
  }
  .cover__figure {
    position: absolute;
    left: 462px;
    top: 480px;
    width: 44px;
    height: 260px;
    background: linear-gradient(180deg, var(--figure) 0%, rgba(42,42,44,0.85) 100%);
    border-radius: 22px 22px 4px 4px;
    opacity: 0.9;
  }
  .title {
    position: absolute;
    left: 20px;
    top: 205px;
    width: 420px;
    text-align: center;
    font-family: "Caveat Brush", cursive;
    font-weight: 400;
    color: var(--ink);
    line-height: 0.9;
  }
  .title__line {
    display: block;
    font-size: 104px;
  }
  .title__joiner {
    display: block;
    font-size: 40px;
    color: var(--ink-accent);
    margin: 2px 0 4px;
  }
  .subtitle-band {
    position: absolute;
    left: 0;
    top: 545px;
    width: 100%;
    height: 38px;
    background: var(--band);
    display: flex;
    align-items: center;
    justify-content: center;
  }
  .subtitle {
    font-family: "Open Sans", sans-serif;
    font-weight: 700;
    font-size: 17px;
    letter-spacing: 0.5px;
    color: var(--band-text);
    text-transform: uppercase;
  }
  .author {
    position: absolute;
    left: 0;
    top: 615px;
    width: 100%;
    text-align: center;
    font-family: "Open Sans", sans-serif;
    font-weight: 600;
    font-size: 15px;
    color: var(--band-text);
  }
</style>
</head>
<body>
  <main class="cover">
    <div class="cover__sky" role="img" aria-label="Pale pink evening sky with a flock of birds flying across it"></div>
    <div class="cover__hand" role="img" aria-label="Photograph of a hand holding a fountain pen, writing the title"></div>
    <div class="cover__landscape" role="img" aria-label="Misty treeline above a calm blue lake"></div>
    <div class="cover__figure" role="img" aria-label="Silhouette of a person standing by the water, seen from behind"></div>

    <h1 class="title">
      <span class="title__line">Chart</span>
      <span class="title__joiner">new</span>
      <span class="title__line">Mornings</span>
    </h1>

    <div class="subtitle-band">
      <p class="subtitle">Step Into a Brighter Season</p>
    </div>

    <p class="author">Martin Olsfield</p>
  </main>
</body>
</html>
```